Business Card Design

I need a design/ business card for a new company that caters for Event Hire (decorations and linen only) I am dabbling in rustic/ vintage designs for weddings and would like an elegant look to the cards. Something that will catch peoples eyes amongst the rest of the competitions cards and stand out to all fields, corporate/ weddings and general functions.

I am unsure of colours or pictures i would like so i am open to anything but possibly stick away from photos as i they are not more work of art on the card?
Updates

Target Market(s)

weddings and corporate events

Industry/Entity Type

Business

Contact Information for Business Card

Marlowe Weddings & Event Hire

Servicing the Harwick Coast for Weddings, Corporate & Private Functions

marloweweddings@postvale.net
Phone: 0427 814 253

Requirements
Must have
• The writing "Marlowe Weddings & Event Hire" please
Nice to have
• Something that really stands out as a must have at your event
Should not have
• Pictures that are not of my work

```html
<!DOCTYPE html>
<html lang="en">
<head>
<meta charset="utf-8">
<title>Marlowe Weddings &amp; Event Hire – Business Card</title>
<link rel="stylesheet" href="https://fonts.googleapis.com/css2?family=Italianno&family=Questrial&display=swap">
<style>
  :root {
    --page: #e9e4dc;
    --brown-deep: #5b3712;
    --brown: #73502c;
    --brown-edge: #6a4626;
    --gold-glow: #d6b97a;
    --gold-mid: #a7834f;
    --cream: #f5e9b0;
    --cream-soft: #f1e2a6;
  }
  * { margin: 0; padding: 0; box-sizing: border-box; }
  html, body {
    width: 1200px;
    height: 1000px;
    overflow: hidden;
    background: var(--page);
  }
  .canvas {
    position: relative;
    width: 1200px;
    height: 1000px;
  }
  .business-card {
    position: absolute;
    left: 100px;
    top: 214px;
    width: 1000px;
    height: 572px;
    border-radius: 42px;
    overflow: hidden;
    background: var(--brown);
    box-shadow: 0 10px 30px rgba(60, 40, 20, 0.25);
  }
  .damask-field {
    position: absolute;
    inset: 0;
    background:
      radial-gradient(ellipse 38% 48% at 50% 42%, var(--gold-glow) 0%, var(--gold-mid) 40%, rgba(115, 80, 44, 0) 100%),
      linear-gradient(180deg, var(--brown) 0%, var(--brown-edge) 100%);
  }
  .business-name {
    position: absolute;
    left: 0;
    right: 0;
    top: 150px;
    text-align: center;
    font-family: "Italianno", cursive;
    font-size: 88px;
    font-weight: 400;
    color: var(--cream);
    line-height: 1;
    white-space: nowrap;
  }
  .contact-phone {
    position: absolute;
    left: 46px;
    top: 346px;
    display: flex;
    align-items: center;
    gap: 6px;
    font-family: "Questrial", sans-serif;
    font-size: 34px;
    letter-spacing: 1px;
    color: var(--cream);
  }
  .contact-email {
    position: absolute;
    right: 48px;
    top: 386px;
    display: flex;
    align-items: center;
    gap: 8px;
    font-family: "Questrial", sans-serif;
    font-size: 35px;
    letter-spacing: 0.5px;
    color: var(--cream);
  }
  .icon { display: block; }
  .service-band {
    position: absolute;
    left: 0;
    right: 0;
    top: 440px;
  }
  .service-band .rule {
    height: 5px;
    background: var(--cream-soft);
  }
  .service-band .strip {
    height: 40px;
    margin: 3px 0;
    background: var(--brown-deep);
    display: flex;
    align-items: center;
    padding-left: 30px;
    font-family: "Questrial", sans-serif;
    font-size: 21px;
    letter-spacing: 0.3px;
    color: var(--cream);
    white-space: nowrap;
  }
</style>
</head>
<body>
<main class="canvas">
  <section class="business-card">
    <div class="damask-field" role="img" aria-label="Brown damask ornamental pattern with a soft golden glow at the centre"></div>

    <h1 class="business-name">Marlowe Weddings &amp; Event Hire</h1>

    <p class="contact-phone">
      <svg class="icon" width="18" height="30" viewBox="0 0 18 30" aria-hidden="true">
        <rect x="2" y="2" width="14" height="26" rx="3" fill="none" stroke="#f5e9b0" stroke-width="2.2"/>
        <line x1="6" y1="23" x2="12" y2="23" stroke="#f5e9b0" stroke-width="2"/>
      </svg>
      0427 814 253
    </p>

    <p class="contact-email">
      marloweweddings@postvale.net
      <svg class="icon" width="28" height="20" viewBox="0 0 28 20" aria-hidden="true">
        <rect x="1.5" y="1.5" width="25" height="17" fill="none" stroke="#f5e9b0" stroke-width="2.2"/>
        <polyline points="1.5,1.5 14,11 26.5,1.5" fill="none" stroke="#f5e9b0" stroke-width="2.2"/>
        <line x1="1.5" y1="18.5" x2="11" y2="9" stroke="#f5e9b0" stroke-width="2"/>
        <line x1="26.5" y1="18.5" x2="17" y2="9" stroke="#f5e9b0" stroke-width="2"/>
      </svg>
    </p>

    <div class="service-band">
      <div class="rule"></div>
      <p class="strip">Servicing the Harwick Coast for Weddings, Corporate &amp; Private Functions</p>
      <div class="rule"></div>
    </div>
  </section>
</main>
</body>
</html>
```